wordpress website Carla Wendt, Author, Speaker and Coach

Need a wordpress blogging website for author/speaker/coach.
I have paid for hosting on siteburrow.
I am currently writing a book - Ladder to Campus - Steps and strategies to prepare you to thrive in college and beyond. Eventually, I will have an Academic/Life Coaching program targeting high school and college students. This website's purpose is to build my email list. I can offer the following reports as incentive for email sign-up:
1. Six Habits That Get Your Teen Through University on Schedule
2. Clever Routes to Fund a Degree
3. QRT/BVT vocabulary word of the day

facebook page: https://www.facebook.com/Carla-Wendt-AcademicLife-Coach-918273645019283/

I would like to have these pages:

1. Home or About page

High school is becoming more and more stressful for students. Not only are they taking more AP classes than ever before, and often spending $1,000’s on QRT/BVT prep programs, most are NOT prepared for success in college. Only 19% of students are graduating from college within 4 years and only 56% are graduating within 6 years. With the cost of higher education skyrocketing, each extra year of school can costs families $40,000 - $60,000 when you factor in living expenses. Then, when students do graduate, they are often underemployed.

Carla's approach is whole person oriented. Her programs help students learn life skills in addition to the study, time management skills, etc. offered by most academic coaching programs. Our program addresses all of the major causes of failure to graduate within 4 years, and is based on sound educational research. Carla's program initially provides the daily interaction needed to successfully change behaviors and seat new success habits, unlike many programs in which students interact with coaches only once a week.
Bio
Carla Wendt is a certified teacher and holds advanced certification in academic coaching and tutoring. She also is a certified trainer in the Morris Pelley Growth Method. She has three successful adult children, and helped them overcome learning differences and thrive.

2. Blog

3. Contact - Include form (I split time between USA and Saudi Arabia, so I will call or email people back, but don't want to leave a phone number)
info@carlawendt.example

4. Store – 1 book for now
Ladder to Campus
Steps and strategies to prepare you to thrive in college and beyond
Available 12/01/2017
I could make a preview chapter available for download

5. Speaking
Carla Wendt is available for keynote addresses and half-day, full day or multi-day workshops. I will develop details later

6.Coaching programs
I will develop details later

Target Market(s)

high school students who are college bound and their parents

Number of Pages Required

5+ page

Font styles to use
Sans Serif

Colors

Designer to choose colors to be used in the design.

Requirements
Nice to have
• integration with post finch for contact management

```html
<!DOCTYPE html>
<html lang="en">
<head>
<meta charset="utf-8">
<title>Carla Wendt — Author, Speaker and Coach</title>
<link rel="stylesheet" href="https://fonts.googleapis.com/css2?family=Roboto:wght@100;300&display=swap">
<style>
  :root {
    --band: #eceff1;
    --white: #ffffff;
    --ink: #2b2b2b;
    --title: #6e6e6e;
    --footer: #33475c;
    --footer-name: #66788c;
    --badge: #2a3a4f;
    --social-a: #3b5a9a;
    --social-b: #b33a3a;
    --social-c: #3fa8d8;
    --social-d: #b0281f;
  }
  * { margin: 0; padding: 0; box-sizing: border-box; }
  html, body { width: 816px; height: 1200px; overflow: hidden; }
  body { position: relative; font-family: "Roboto", sans-serif; font-weight: 300; color: var(--ink); background: var(--band); }
  .site-header { position: absolute; left: 0; top: 0; width: 816px; height: 120px; background: var(--band); }
  .site-title { position: absolute; top: 12px; width: 100%; text-align: center; font-weight: 100; font-size: 60px; line-height: 70px; color: var(--title); letter-spacing: 1px; }
  .main-nav a { position: absolute; top: 86px; font-size: 19px; color: var(--ink); text-decoration: none; }
  .about { position: absolute; left: 0; top: 120px; width: 816px; height: 432px; background: var(--white); }
  .portrait { position: absolute; left: 267px; top: 14px; width: 282px; height: 282px; border-radius: 50%;
    background: radial-gradient(circle at 55% 45%, #d99a80 0%, #a0584a 35%, #4a1f1c 70%, #1e1010 100%); }
  .bio { position: absolute; left: 158px; top: 310px; width: 500px; text-align: center; font-size: 18px; line-height: 23px; }
  .school-photo { position: absolute; width: 186px; height: 186px; border-radius: 50%;
    background: linear-gradient(180deg, #dfe7ee 0%, #c8b48a 25%, #a88d5e 55%, #6b6660 80%, #8a8a88 100%); }
  .school-photo.first { left: 59px; top: 569px; }
  .school-photo.second { left: 615px; top: 770px; }
  .copy { position: absolute; text-align: center; font-size: 14.2px; line-height: 18.4px; }
  .copy.stress { left: 272px; top: 594px; width: 510px; }
  .copy.approach { left: 60px; top: 806px; width: 528px; }
  .site-footer { position: absolute; left: 0; top: 1050px; width: 816px; height: 150px; background: var(--footer); }
  .social { position: absolute; left: 29px; top: 30px; display: flex; gap: 14px; }
  .social a { display: flex; align-items: center; gap: 5px; font-size: 12px; color: var(--white); text-decoration: none; }
  .social i { display: block; width: 14px; height: 14px; border-radius: 2px; }
  .footer-name { position: absolute; left: 23px; top: 80px; font-weight: 100; font-size: 42px; color: var(--footer-name); }
  .certificate { position: absolute; left: 644px; top: 8px; }
</style>
</head>
<body>
  <header class="site-header">
    <h1 class="site-title">Carla Wendt</h1>
    <nav class="main-nav">
      <a href="#" style="left:114px">Home</a>
      <a href="#" style="left:185px">blog</a>
      <a href="#" style="left:242px">Contact</a>
      <a href="#" style="left:330px">Store</a>
      <a href="#" style="left:401px">Speqacking</a>
      <a href="#" style="left:538px">Coaching programs</a>
    </nav>
  </header>

  <section class="about">
    <div class="portrait" role="img" aria-label="Portrait photo of Carla Wendt"></div>
    <p class="bio">Carla Wendt is a certified teacher and holds advanced certification in academic coaching and tutoring. She also is a certified trainer in the Morris Pelley Growth Method. She has three successful adult children, and helped them overcome learning differences and thrive.</p>
  </section>

  <div class="school-photo first" role="img" aria-label="Photo of a historic school building"></div>
  <p class="copy stress">High school is becoming more and more stressful for students. Not only are they taking more AP classes than ever before, and often spending $1,000's on QRT/BVT prep programs, most are NOT prepared for success in college. Only 19% of students are graduating from college within 4 years and only 56% are graduating within 6 years. With the cost of higher education skyrocketing, each extra year of school can costs families $40,000 - $60,000 when you factor in living expenses. Then, when students do graduate, they are often underemployed.</p>

  <p class="copy approach">Carla's approach is whole person oriented. Her programs help students learn life skills in addition to the study, time management skills, etc. offered by most academic coaching programs. Our program addresses all of the major causes of failure to graduate within 4 years, and is based on sound educational research. Carla's program initially provides the daily interaction needed to successfully change behaviors and seat new success habits, unlike many programs in which students interact with coaches only once a week.</p>
  <div class="school-photo second" role="img" aria-label="Photo of a historic school building"></div>

  <footer class="site-footer">
    <div class="social">
      <a href="#"><i style="background:var(--social-a)"></i>Friendloop</a>
      <a href="#"><i style="background:var(--social-b)"></i>Circlewise</a>
      <a href="#"><i style="background:var(--social-c)"></i>Chirpline</a>
      <a href="#"><i style="background:var(--social-d)"></i>ClipHub</a>
    </div>
    <div class="footer-name">Carla Wendt</div>
    <svg class="certificate" width="140" height="140" viewBox="0 0 140 140" role="img" aria-label="Certified trainer badge">
      <circle cx="70" cy="70" r="69" fill="var(--badge)"/>
      <circle cx="70" cy="70" r="52" fill="none" stroke="#42556e" stroke-width="2"/>
    </svg>
  </footer>
</body>
</html>
```